FREE SOCIAL SECURITY DISABILITY CLAIM EVALUATION - Ad Banners & Email Marketing Creatives

Looking for design of ad banners and email creative for my Social Security Disability Insurance Benefits Application, Denial, & Appeals Help website. Call to action based email focused on conveying brand, messaging of "Are you out of work due to a disability? You may qualify for up to $2,642 per month in Social Security Disability benefits!" and "ACT NOW: Check Your Eligibility" Call to action of 'Get Your FREE Evaluation' or 'Fast, FREE, No Obligation Evaluation' or 'Confirm My Eligibility Now!' or 'Start My FREE Evaluation' or 'Confirm My Eligibility Now!'. Can use any messaging and images from the current website:
https://relief-filingdesk.com/

Please focus on imaging that matches the site. The final Ad Banners must be delivered in both JPG and PSD file formats. Ad Banners must follow OMC standards.

We need Ad Banners in the following sizes.
728x90
300x250
336x280
160x600
1200x628
600x600
1080x1080
Email

Target Market(s)
People in the US between the ages 48-63 looking for Social Security Disability Insurance Benefits Application, Denial, & Appeals Help. Get connected to a local Social Security Disability legal representative for a free, no-obligation evaluation. Find out if you are eligible to receive financial compensation for as much as $2,642 a month!

Should not be cookie cutter. Stick to simple yet official looking.

The final Email creative must be done in responsive HTML as well as text for easy use and include Email Opt Out link etc.

Target Market(s)

Americans that are between the ages 48-63 that have a physical condition that prevents them from working. Many times the physical condition is a result of an injury.

Coding

Coded - Design and coding required

Font styles to use
Sans Serif

Requirements
Must have
• A strong call to action.
Should not have
• No photos of people in wheelchairs.

```html
<!DOCTYPE html>
<html lang="en">
<head>
<meta charset="utf-8">
<title>Disability Benefits Evaluation – Ad Banners</title>
<link href="https://fonts.googleapis.com/css2?family=Montserrat:wght@800&family=Roboto:wght@300;500;700&display=swap" rel="stylesheet">
<style>
  :root {
    --board: #ebebeb;
    --navy: #06506f;
    --ink: #111418;
    --muted: #4a4f55;
    --white: #ffffff;
    --sky: #8fbcd1;
    --mist: #c7dbe4;
  }
  * { margin: 0; padding: 0; box-sizing: border-box; }
  html, body { width: 1200px; height: 2254px; overflow: hidden; background: var(--board); }
  body { position: relative; font-family: "Roboto", Arial, sans-serif; }

  .banner { position: absolute; overflow: hidden; }
  .banner svg.art { position: absolute; left: 0; top: 0; }

  .headline {
    position: absolute;
    font-family: "Montserrat", "Arial Black", sans-serif;
    font-weight: 800;
    text-transform: uppercase;
    color: var(--ink);
    letter-spacing: 0.03em;
  }
  .act-line { position: absolute; color: var(--muted); font-weight: 300; white-space: nowrap; }
  .act-line strong { font-weight: 500; color: var(--ink); }
  .act-line .sep { font-weight: 700; color: var(--ink); margin: 0 0.9em; }

  .cta {
    position: absolute;
    display: flex; align-items: center; justify-content: center;
    width: 219px; height: 48px;
    background: var(--navy);
    color: var(--white);
    font-weight: 700;
    font-size: 13.5px;
    text-transform: uppercase;
    border-radius: 2px;
    letter-spacing: 0.01em;
  }

  /* Landscape banner */
  .banner--wide { left: 120px; top: 119px; width: 960px; height: 502px; }
  .banner--wide .headline { left: 54px; top: 126px; width: 440px; font-size: 19.8px; line-height: 32px; }
  .banner--wide .act-line { left: 54px; top: 274px; font-size: 14px; }
  .banner--wide .cta { left: 53px; top: 323px; }

  /* Square banner */
  .banner--square { left: 168px; top: 718px; width: 864px; height: 864px; }
  .banner--square .headline { left: 46px; top: 58px; width: 540px; font-size: 24px; line-height: 37.6px; }
  .banner--square .act-line { left: 46px; top: 226px; font-size: 15px; }
  .banner--square .cta { left: 45px; top: 277px; }

  /* Email / small square */
  .banner--email { left: 360px; top: 1655px; width: 480px; height: 480px; background: var(--sky); }
  .banner--email .headline {
    left: 0; top: 17px; width: 480px; text-align: center;
    font-size: 13.6px; line-height: 22.3px; color: var(--white);
  }
  .banner--email .act-line { left: 0; width: 480px; text-align: center; top: 127px; font-size: 14px; color: var(--white); }
  .banner--email .act-line strong, .banner--email .act-line .sep { color: var(--white); }
  .banner--email .cta { left: 130px; top: 163px; }
</style>
</head>
<body>

<section class="banner banner--wide">
  <svg class="art" width="960" height="502" viewBox="0 0 960 502">
    <defs>
      <linearGradient id="wideBg" x1="0" y1="0" x2="0" y2="1">
        <stop offset="0" stop-color="#f8efe8"/>
        <stop offset="0.55" stop-color="#fbf9f7"/>
        <stop offset="1" stop-color="#e8eef4"/>
      </linearGradient>
      <radialGradient id="wideGlow" cx="0.35" cy="0.1" r="0.5">
        <stop offset="0" stop-color="#f2dccd" stop-opacity="0.7"/>
        <stop offset="1" stop-color="#f2dccd" stop-opacity="0"/>
      </radialGradient>
      <linearGradient id="wideWall" x1="0" y1="0" x2="1" y2="0">
        <stop offset="0" stop-color="#d8d6d6"/>
        <stop offset="0.5" stop-color="#b9c2c6"/>
        <stop offset="1" stop-color="#a9b4b9"/>
      </linearGradient>
      <radialGradient id="wideLight" cx="0.55" cy="0.7" r="0.55">
        <stop offset="0" stop-color="#f7f6f7"/>
        <stop offset="0.6" stop-color="#e6e7ea" stop-opacity="0.8"/>
        <stop offset="1" stop-color="#e6e7ea" stop-opacity="0"/>
      </radialGradient>
      <radialGradient id="wideWarm" cx="0.6" cy="0.35" r="0.3">
        <stop offset="0" stop-color="#e9c8b4" stop-opacity="0.75"/>
        <stop offset="1" stop-color="#e9c8b4" stop-opacity="0"/>
      </radialGradient>
      <linearGradient id="wideShade" x1="0" y1="0" x2="0" y2="1">
        <stop offset="0.6" stop-color="#5c6f86" stop-opacity="0"/>
        <stop offset="1" stop-color="#5c6f86" stop-opacity="0.45"/>
      </linearGradient>
      <clipPath id="wideClip"><polygon points="550,0 960,0 960,502 500,502"/></clipPath>
    </defs>
    <rect width="960" height="502" fill="url(#wideBg)" role="img" aria-label="Faded background photo of paperwork and a pen on a desk"/>
    <rect width="960" height="502" fill="url(#wideGlow)"/>
    <g clip-path="url(#wideClip)" role="img" aria-label="Photo of a smiling caregiver with her hand on the shoulder of an older woman">
      <rect x="480" width="480" height="502" fill="url(#wideWall)"/>
      <rect x="480" width="480" height="502" fill="url(#wideLight)"/>
      <rect x="480" width="480" height="502" fill="url(#wideWarm)"/>
      <rect x="480" width="480" height="502" fill="url(#wideShade)"/>
    </g>
    <polygon points="554,0 578,0 504,502 498,502" fill="var(--navy)"/>
  </svg>
  <h1 class="headline">Are you out of work due to a disability? You may qualify for up to $2,642 per month in Social Security Disability benefits!</h1>
  <p class="act-line"><strong>ACT NOW</strong><span class="sep">:</span>Check Your Eligibility Now.</p>
  <a class="cta">Get Your Free Evaluation</a>
</section>

<section class="banner banner--square">
  <svg class="art" width="864" height="864" viewBox="0 0 864 864">
    <defs>
      <linearGradient id="squareBg" x1="0" y1="0" x2="1" y2="1">
        <stop offset="0" stop-color="#c2d6df"/>
        <stop offset="1" stop-color="#d3e3ea"/>
      </linearGradient>
      <radialGradient id="squareHaze" cx="0.3" cy="0.55" r="0.4">
        <stop offset="0" stop-color="#e3eef2" stop-opacity="0.8"/>
        <stop offset="1" stop-color="#e3eef2" stop-opacity="0"/>
      </radialGradient>
      <linearGradient id="squareRoom" x1="0" y1="0" x2="1" y2="1">
        <stop offset="0" stop-color="#f6f7f8"/>
        <stop offset="0.5" stop-color="#eceeee"/>
        <stop offset="1" stop-color="#dfe2e3"/>
      </linearGradient>
      <radialGradient id="squareShirt" cx="0.74" cy="0.45" r="0.2">
        <stop offset="0" stop-color="#9fd3d6" stop-opacity="0.85"/>
        <stop offset="1" stop-color="#9fd3d6" stop-opacity="0"/>
      </radialGradient>
      <radialGradient id="squareDark" cx="0.72" cy="0.8" r="0.32">
        <stop offset="0" stop-color="#5d6266" stop-opacity="0.7"/>
        <stop offset="1" stop-color="#5d6266" stop-opacity="0"/>
      </radialGradient>
      <radialGradient id="squareChair" cx="0.45" cy="0.58" r="0.16">
        <stop offset="0" stop-color="#c9cacd" stop-opacity="0.8"/>
        <stop offset="1" stop-color="#c9cacd" stop-opacity="0"/>
      </radialGradient>
      <clipPath id="squareClip"><path d="M864,49 C520,140 140,470 37,864 L864,864 Z"/></clipPath>
    </defs>
    <rect width="864" height="864" fill="url(#squareBg)" role="img" aria-label="Faded background photo of a home interior"/>
    <rect width="864" height="864" fill="url(#squareHaze)"/>
    <g clip-path="url(#squareClip)" role="img" aria-label="Photo of a young woman seated in a bright living room">
      <rect width="864" height="864" fill="url(#squareRoom)"/>
      <rect width="864" height="864" fill="url(#squareChair)"/>
      <rect width="864" height="864" fill="url(#squareShirt)"/>
      <rect width="864" height="864" fill="url(#squareDark)"/>
    </g>
    <path d="M0,864 C50,640 190,470 355,352 C210,480 95,650 37,864 Z" fill="var(--navy)"/>
  </svg>
  <h1 class="headline">Are you out of work due to a disability? You may qualify for up to $2,642 per month in Social Security Disability benefits!</h1>
  <p class="act-line"><strong>ACT NOW</strong><span class="sep">:</span>Check Your Eligibility Now.</p>
  <a class="cta">Get Your Free Evaluation</a>
</section>

<section class="banner banner--email">
  <svg class="art" width="480" height="480" viewBox="0 0 480 480">
    <defs>
      <linearGradient id="emailRoom" x1="0" y1="0" x2="0" y2="1">
        <stop offset="0" stop-color="#f6f7f8"/>
        <stop offset="1" stop-color="#e4e8ec"/>
      </linearGradient>
      <radialGradient id="emailScrubs" cx="0.12" cy="0.95" r="0.35">
        <stop offset="0" stop-color="#5fa3d6" stop-opacity="0.9"/>
        <stop offset="1" stop-color="#5fa3d6" stop-opacity="0"/>
      </radialGradient>
      <radialGradient id="emailShirts" cx="0.65" cy="0.85" r="0.35">
        <stop offset="0" stop-color="#8fa9c0" stop-opacity="0.75"/>
        <stop offset="1" stop-color="#8fa9c0" stop-opacity="0"/>
      </radialGradient>
      <radialGradient id="emailSofa" cx="0.95" cy="0.8" r="0.2">
        <stop offset="0" stop-color="#b9bec3" stop-opacity="0.7"/>
        <stop offset="1" stop-color="#b9bec3" stop-opacity="0"/>
      </radialGradient>
      <clipPath id="emailClip"><path d="M0,205 Q240,287 480,205 V480 H0 Z"/></clipPath>
    </defs>
    <g clip-path="url(#emailClip)" role="img" aria-label="Photo of a care worker greeting an older couple on a sofa">
      <rect width="480" height="480" fill="url(#emailRoom)"/>
      <rect width="480" height="480" fill="url(#emailSofa)"/>
      <rect width="480" height="480" fill="url(#emailShirts)"/>
      <rect width="480" height="480" fill="url(#emailScrubs)"/>
    </g>
    <path d="M0,183 Q240,341 480,183 L480,205 Q240,287 0,205 Z" fill="var(--navy)"/>
  </svg>
  <h1 class="headline">Are you out of work due to a<br>disability? You may qualify for<br>up to $2,642 per month in social<br>security disability benefits!</h1>
  <p class="act-line"><strong>ACT NOW</strong><span class="sep">:</span>Check Your Eligibility Now.</p>
  <a class="cta">Get Your Free Evaluation</a>
</section>

</body>
</html>
```